Corporate-Design für Altreifenentsorgung/Container
Zielgruppe
Wir sind ein Familienunternehmen das zum Jahreswechsel vom Gründer Ferdinand Wunsiedl an seinen Sohn Thomas Wunsiedl übergeben wurde. Also Inhabergeführtes Familienunternehmen ist uns der persönliche Kontakt mit den Kunden sehr wichtig. Gemeinsam versuchen wir immer eine Individuelle Lösung zu finden um den Anforderungen der Kunden exakt entsprechen.
Wir betreiben drei Geschäftsbereiche:
- Heu & Stroh : Wir beliefern Landwirte, Reitställe, Tierparks, usw. ganzjährig mit hochwertigem Heu, Stroh, und anderen Futtermittel auch in Bio-Qualität. Die Lieferung zu den Kunden in Deutschland, Österreich, Italien und der Schweiz erfolgt mit eigenen LKWs
- Altreifenentsorgung: Wir entsorgen alle Arten von Altreifen von KFZ/LKW-Werkstätten, Speditionen, landwirtschaftlichen Betrieben, Bauunternehmen, usw.... Die Reifen werden von uns direkt beim Kunden abgeholt und einer Fach- und Umweltgerechten Verwertung zugeführt.
- Container: Unser jüngster Geschäftsbereich. Wir vertreiben neue und gebrauchte Abrollcontainer für den Transport und zur Lagerung von Schotter, Abfällen, Baumaschinen, Baustoffen, usw. Besonderheit hierbei ist, dass wir einen großen Lagerbestand an neuen und gebrauchten Containern haben. Somit können sich unsere Kunden sofort verfügbare Modelle ohne Lieferzeit aussuchen und sofort einsetzen. Außerdem vermieten wir diese Container auch (Containerdienst)
weitere Information finden Sie unter www.ferdinand-wunsiedl.de
Aufgabenstellung
Wir wünschen uns ein Zeitgemäßes Logo in dem man jedoch erkennen kann die' Verwandtschaft' zur alten Firma erkennen kann. So sollten sich die Farben gelb und grün im neuen Logo wiederfinden.
Der Slogan 'Natürlich. Zuverlässig. Handeln.' sollte im Logo enthalten sein
Die Geschäftsbereiche 'Heu & Stroh - Altreifenentsorgung - Container' können, müssen aber nicht im Logo erwähnt werden. Falls sie jedoch nicht im Logo erwähnt werden, sollten Sie jedoch auf Briefpapier und Visitenkarten gedruckt werden.
Auf der Visitenkarte sollte eine V-Card als QR-Code abgebildet sein.
Weitere Daten für Visitenkarte:
Name: Thomas Wunsiedl
Adresse: Kastanienweg 17, 85599 Pöringhof
Tel: +49 89-7712058
Fax: +49 89-7719058
Mob: +49 152-06137482
web: www.wunsiedl.bayern
e-mail: wird nachgereicht
zusätzliche Angaben auf Briefpapier:
Bank: Raiffeisenkasse Kelbachtal eG
IBAN: DE41 7021 3357 0004 6215 80
BIC: GENO DEF1 KBT
Öko-Kontrollstellennummer: DE-ÖKO-091
UID: wird nachgereicht
Steuer-Nr.: wird nachgereicht

```html
<!DOCTYPE html>
<html lang="de">
<head>
<meta charset="utf-8">
<title>Thomas Wunsiedl – Visitenkarte</title>
<link rel="stylesheet" href="https://fonts.googleapis.com/css2?family=Open+Sans:wght@400;600&display=swap">
<style>
  :root {
    --bg: #e4e4e4;
    --paper: #f7f7f5;
    --green: #7cb84a;
    --yellow: #f1cf1f;
    --ink: #4d4d4d;
    --ink-soft: #6b6b6b;
  }
  * { margin: 0; padding: 0; box-sizing: border-box; }
  html, body {
    width: 1200px; height: 899px; overflow: hidden;
    background: var(--bg);
    font-family: "Open Sans", Arial, sans-serif;
    color: var(--ink);
  }
  .stage {
    position: relative; width: 1200px; height: 899px;
    display: flex; align-items: center; justify-content: center; gap: 40px;
  }
  .card {
    position: relative; width: 540px; height: 350px;
    background: var(--paper);
    box-shadow: 0 6px 18px rgba(0,0,0,.12);
    overflow: hidden;
  }
  .card .bands { position: absolute; inset: 0; }

  /* back side */
  .brand-block {
    position: absolute; left: 0; right: 0; top: 120px;
    display: flex; flex-direction: column; align-items: center; gap: 8px;
  }
  .brand {
    display: flex; align-items: center; gap: 12px;
  }
  .brand-mark { width: 26px; height: 26px; background: var(--yellow); }
  .brand-name {
    font-size: 30px; font-weight: 600; color: var(--ink); letter-spacing: .2px;
  }
  .slogan { font-size: 12px; color: var(--ink-soft); letter-spacing: .6px; }

  /* front side */
  .front .brand { position: absolute; left: 44px; top: 156px; }
  .front .brand-name { font-size: 24px; color: var(--green); }
  .contact {
    position: absolute; left: 300px; top: 70px;
  }
  .contact-name { font-size: 24px; font-weight: 600; color: var(--ink); margin-bottom: 12px; }
  .contact-lines { list-style: none; font-size: 11px; line-height: 1.7; color: var(--ink-soft); }
</style>
</head>
<body>
<main class="stage">

  <section class="card back" aria-label="Visitenkarte Rückseite">
    <div class="brand-block">
      <div class="brand">
        <span class="brand-mark"></span>
        <span class="brand-name">Thomas Wunsiedl</span>
      </div>
      <p class="slogan">Natürlich. Zuverlässig. Handeln.</p>
    </div>
  </section>

  <section class="card front" aria-label="Visitenkarte Vorderseite">
    <svg class="bands" viewBox="0 0 540 350" aria-hidden="true">
      <polygon points="0,52 200,52 176,72 0,72" fill="var(--green)"/>
      <polygon points="380,290 540,290 540,310 356,310" fill="var(--yellow)"/>
    </svg>
    <div class="brand">
      <span class="brand-mark"></span>
      <span class="brand-name">Thomas Wunsiedl</span>
    </div>
    <div class="contact">
      <h1 class="contact-name">Thomas Wunsiedl</h1>
      <ul class="contact-lines">
        <li>Kastanienweg 17, 85599 Pöringhof</li>
        <li>Tel.: +49 89-7712058</li>
        <li>Fax: +49 89-7719058</li>
        <li>Mobil: +49 152-06137482</li>
        <li>web: www.wunsiedl.bayern</li>
      </ul>
    </div>
  </section>

</main>
</body>
</html>
```